Larkspur Sports Medicine

I am a busy athletic trainer at a high school in Colorado

I totally forgot to put in my email address : rbellamy@hvsd44.org I MUST have my email address in there.

High School

Rob Bellamy, MSS, ATC/R, CSCS
Thistlewood High School
• Head Athletic Trainer
• Athletics Archives Manager
• Athletic Concession Stand Manager
• Athletic Equipment Manager
Harlan Valley School District
• Athletic Training Group Coordinator
United Sports Therapists Guild
• Director -- District 7

4118 W Cedar Knoll Road
Parker, CO 80197

Cell — 720-555-0148
Office — 303-555-0172
Fax — 303-555-0189

• I like Lucidia Sans as my font (that is what I have on my letterhead etc.)

Honestly I am not that picky. I just want to have all of my information fit and I would like the logo on there as well.

```html
<!DOCTYPE html>
<html lang="en">
<head>
<meta charset="utf-8">
<title>Larkspur Sports Medicine — Business Card</title>
<link rel="stylesheet" href="https://fonts.googleapis.com/css2?family=Open+Sans:wght@400;600;700&display=swap">
<style>
  :root {
    --page-bg: #e9e9e9;
    --orange-light: #e8832c;
    --orange-dark: #c4621e;
    --red: #c0202a;
    --red-dark: #a8161f;
    --wave-line: #e6e6e6;
    --ink: #2b2320;
    --ink-soft: #3d3431;
    --white: #ffffff;
  }
  html, body {
    margin: 0;
    padding: 0;
    width: 1200px;
    height: 1200px;
    overflow: hidden;
    background: var(--page-bg);
    font-family: "Open Sans", "Lucida Sans", sans-serif;
  }
  .card {
    position: absolute;
    left: 75px;
    top: 300px;
    width: 1050px;
    height: 600px;
    overflow: hidden;
    box-shadow: 0 10px 30px rgba(0,0,0,0.18);
  }
  .card-bg {
    position: absolute;
    inset: 0;
    width: 100%;
    height: 100%;
  }
  .brand {
    position: absolute;
    left: 70px;
    top: 78px;
    display: flex;
    align-items: center;
    gap: 14px;
  }
  .brand-dot {
    width: 22px;
    height: 22px;
    border-radius: 50%;
    background: var(--red);
  }
  .brand-name {
    font-size: 34px;
    font-weight: 700;
    color: var(--red);
    line-height: 1.1;
    max-width: 330px;
  }
  .contact {
    position: absolute;
    left: 630px;
    top: 92px;
    color: var(--ink);
  }
  .contact-name {
    font-size: 38px;
    font-weight: 600;
    margin: 0;
    line-height: 1.1;
  }
  .contact-creds {
    font-size: 15px;
    margin: 2px 0 16px;
    color: var(--ink-soft);
  }
  .contact-address {
    font-size: 24px;
    line-height: 1.25;
    margin: 0 0 12px;
  }
  .contact-list {
    list-style: none;
    margin: 0;
    padding: 0;
    font-size: 24px;
    line-height: 1.3;
  }
  .contact-list li {
    display: flex;
    align-items: center;
    gap: 12px;
  }
  .contact-list .contact-email {
    font-size: 22px;
  }
  .contact-icon {
    width: 22px;
    height: 22px;
    flex: none;
  }
  .roles {
    position: absolute;
    list-style: none;
    margin: 0;
    padding: 0;
    color: var(--white);
    font-size: 19px;
    line-height: 1.35;
  }
  .roles li::before {
    content: "•";
    margin-right: 8px;
  }
  .roles-school {
    left: 60px;
    top: 300px;
  }
  .roles-district {
    left: 440px;
    top: 470px;
  }
</style>
</head>
<body>
  <article class="card">
    <svg class="card-bg" viewBox="0 0 1050 600" preserveAspectRatio="none" aria-hidden="true">
      <defs>
        <linearGradient id="orangeFill" x1="0" y1="0" x2="1" y2="0">
          <stop offset="0" stop-color="var(--orange-light)"/>
          <stop offset="1" stop-color="var(--orange-dark)"/>
        </linearGradient>
        <linearGradient id="redFill" x1="0" y1="0" x2="1" y2="1">
          <stop offset="0" stop-color="var(--red)"/>
          <stop offset="1" stop-color="var(--red-dark)"/>
        </linearGradient>
      </defs>
      <rect width="1050" height="600" fill="url(#orangeFill)"/>
      <path d="M0,240 C240,180 430,330 640,440 C780,510 900,470 1050,400 L1050,600 L0,600 Z" fill="url(#redFill)"/>
      <path d="M0,240 C240,180 430,330 640,440 C780,510 900,470 1050,400" fill="none" stroke="var(--wave-line)" stroke-width="7"/>
    </svg>

    <div class="brand">
      <span class="brand-dot"></span>
      <span class="brand-name">Larkspur Sports Medicine</span>
    </div>

    <div class="contact">
      <h1 class="contact-name">Rob Bellamy</h1>
      <p class="contact-creds">MSS, ATC/R, CSCS</p>
      <p class="contact-address">4118 W Cedar Knoll Road<br>Parker, CO 80197</p>
      <ul class="contact-list">
        <li>
          <svg class="contact-icon" viewBox="0 0 22 22" aria-label="Cell">
            <rect width="22" height="22" rx="4" fill="var(--red)"/>
            <rect x="7" y="4" width="8" height="14" rx="1.5" fill="none" stroke="var(--white)" stroke-width="1.8"/>
          </svg>
          720-555-0148
        </li>
        <li>
          <svg class="contact-icon" viewBox="0 0 22 22" aria-label="Office">
            <rect width="22" height="22" rx="4" fill="var(--red)"/>
            <path d="M6 5 L9 5 L10 9 L8.5 10.5 C9.5 12.5 10.5 13.5 12.5 14.5 L14 13 L18 14 L18 17 C11 17 5 11 6 5 Z" fill="var(--white)"/>
          </svg>
          303-555-0172
        </li>
        <li>
          <svg class="contact-icon" viewBox="0 0 22 22" aria-label="Fax">
            <rect width="22" height="22" rx="4" fill="var(--red)"/>
            <rect x="5" y="9" width="12" height="8" rx="1" fill="var(--white)"/>
            <rect x="7.5" y="4" width="7" height="5" fill="none" stroke="var(--white)" stroke-width="1.6"/>
          </svg>
          303-555-0189
        </li>
        <li class="contact-email">
          <svg class="contact-icon" viewBox="0 0 22 22" aria-label="Email">
            <rect width="22" height="22" rx="4" fill="var(--red)"/>
            <rect x="4" y="6" width="14" height="10" rx="1" fill="none" stroke="var(--white)" stroke-width="1.6"/>
            <path d="M4.5 6.5 L11 12 L17.5 6.5" fill="none" stroke="var(--white)" stroke-width="1.6"/>
          </svg>
          rbellamy@hvsd44.org
        </li>
      </ul>
    </div>

    <ul class="roles roles-school">
      <li>Thistlewood High School</li>
      <li>Head Athletic Trainer</li>
      <li>Athletics Archives Manager</li>
      <li>Athletic Concession Stand Manager</li>
      <li>Athletic Equipment Manager</li>
    </ul>

    <ul class="roles roles-district">
      <li>Harlan Valley School District</li>
      <li>Athletic Training Group Coordinator</li>
      <li>United Sports Therapists Guild</li>
      <li>Director -- District 7</li>
    </ul>
  </article>
</body>
</html>
```